Brell Harbor Company Business Cards

Front and Back Business Card - logo and text setup - cool design. I need workable photoshop or illustrator files so I can setup each employee card with design that is created
Updates

Hi everyone, thank you for the great entries. Please no more white and blue cards - there are so many already - black and silver only now please. thanks!

Target Market(s)

Construction Industry - Facility Managers

Industry/Entity Type

Construction

Contact Information for Business Card

I really like contemporary simplistic looks - clean neat....not opposed to seeing some black backrounds

Requirements
Must have
• Logo/website address with design on front only - www.brellharbor-example.com (logo attached)
• Back:
• Name/Title/Company Address/Phone/email address
Nice to have
• Cool design
Should not have
• Nothing gimmicky like Fire or Water - since we are a Fire Protection company - it has all been done

```html
<!DOCTYPE html>
<html lang="en">
<head>
<meta charset="utf-8">
<title>Brell Harbor Company – Business Cards</title>
<link rel="stylesheet" href="https://fonts.googleapis.com/css2?family=Arimo:wght@400;700&display=swap">
<style>
  :root {
    --page-bg: #e6e6e6;
    --black: #0b0b0d;
    --graphite: #4e5157;
    --brand-ink: #16171a;
    --title-silver: #c4c8ce;
    --white: #ffffff;
    --band-silver: #d6d8dc;
    --metal-dark: #7c7f85;
    --metal-light: #eceef0;
    --metal-mid: #b3b6bc;
  }
  html, body {
    margin: 0;
    width: 1200px;
    height: 1200px;
    overflow: hidden;
    background: var(--page-bg);
    font-family: "Arimo", Arial, sans-serif;
  }
  .canvas { position: relative; width: 1200px; height: 1200px; }
  .card {
    position: absolute;
    left: 150px;
    width: 900px;
    height: 514px;
    overflow: hidden;
    background: var(--black);
    box-shadow: 0 10px 28px rgba(0,0,0,.28);
  }
  .card--back { top: 60px; }
  .card--front { top: 626px; }
  .card svg.art { position: absolute; inset: 0; width: 900px; height: 514px; }

  .wordmark {
    position: absolute;
    margin: 0;
    font-weight: 700;
    color: var(--brand-ink);
    letter-spacing: -0.5px;
    line-height: 1.05;
  }
  .card--back .wordmark { left: 48px; top: 60px; font-size: 30px; width: 260px; }
  .card--front .wordmark { left: 320px; top: 178px; font-size: 50px; white-space: nowrap; }

  .holder { position: absolute; right: 58px; top: 150px; text-align: right; }
  .holder__name { margin: 0; color: var(--white); font-weight: 700; font-size: 34px; letter-spacing: 1px; line-height: 1; }
  .holder__title { margin: 6px 0 0; color: var(--title-silver); font-weight: 700; font-size: 25px; letter-spacing: 1px; line-height: 1; }

  .address { position: absolute; right: 58px; top: 258px; margin: 0; text-align: right; color: var(--white); font-weight: 700; font-size: 20px; line-height: 1.35; font-style: normal; }

  .contact { position: absolute; width: 280px; text-align: center; color: var(--white); font-size: 17px; white-space: nowrap; }
  .contact svg { display: block; margin: 0 auto 18px; width: 50px; height: 50px; }
  .contact--email { left: 40px; top: 404px; }
  .contact--web { left: 330px; top: 382px; }
  .contact--phone { left: 600px; top: 342px; }

  .front-web { position: absolute; left: 0; right: 0; top: 414px; text-align: center; color: var(--white); font-size: 20px; }
  .front-web svg { display: block; margin: 0 auto 14px; width: 34px; height: 34px; }
</style>
</head>
<body>
<div class="canvas">

  <svg width="0" height="0" style="position:absolute">
    <defs>
      <linearGradient id="metal" x1="0" y1="0" x2="1" y2="0.3">
        <stop offset="0" stop-color="var(--metal-dark)"/>
        <stop offset="0.35" stop-color="var(--metal-light)"/>
        <stop offset="0.7" stop-color="var(--metal-mid)"/>
        <stop offset="1" stop-color="var(--metal-dark)"/>
      </linearGradient>
      <linearGradient id="fold-shade" x1="0" y1="0" x2="1" y2="1">
        <stop offset="0" stop-color="#000" stop-opacity="0"/>
        <stop offset="1" stop-color="#000" stop-opacity="0.55"/>
      </linearGradient>
    </defs>
  </svg>

  <!-- Back: holder details -->
  <section class="card card--back" aria-label="Card back with contact details">
    <svg class="art" viewBox="0 0 900 514" aria-hidden="true">
      <polygon points="0,0 560,0 0,480" fill="url(#metal)"/>
      <polygon points="560,0 600,0 0,515 0,480" fill="url(#fold-shade)"/>
      <polygon points="760,0 900,0 900,92 600,138" fill="var(--graphite)"/>
      <polygon points="430,262 900,228 900,370 200,430" fill="var(--graphite)"/>
    </svg>
    <p class="wordmark">Brell Harbor Company</p>
    <div class="holder">
      <p class="holder__name">NAME SURNAME</p>
      <p class="holder__title">MANAGER</p>
    </div>
    <address class="address">Adress. Street. number<br>City CODE</address>
    <div class="contact contact--email">
      <svg viewBox="0 0 50 50"><circle cx="25" cy="25" r="25" fill="var(--white)"/><rect x="13" y="17" width="24" height="16" fill="var(--black)"/><polyline points="14,18 25,27 36,18" fill="none" stroke="var(--white)" stroke-width="2"/></svg>
      contact @ brellharbor-example.com
    </div>
    <div class="contact contact--web">
      <svg viewBox="0 0 50 50"><circle cx="25" cy="25" r="25" fill="var(--white)"/><g fill="none" stroke="var(--black)" stroke-width="2"><circle cx="25" cy="25" r="13"/><ellipse cx="25" cy="25" rx="6" ry="13"/><line x1="12" y1="25" x2="38" y2="25"/><line x1="14" y1="18" x2="36" y2="18"/><line x1="14" y1="32" x2="36" y2="32"/></g></svg>
      www.brellharbor-example.com
    </div>
    <div class="contact contact--phone">
      <svg viewBox="0 0 50 50"><circle cx="25" cy="25" r="25" fill="var(--white)"/><rect x="18" y="12" width="14" height="26" rx="2" fill="var(--black)"/><rect x="20" y="15" width="10" height="18" fill="var(--white)"/></svg>
      +33 333 333 333
    </div>
  </section>

  <!-- Front: name and website -->
  <section class="card card--front" aria-label="Card front with company name">
    <svg class="art" viewBox="0 0 900 514" aria-hidden="true">
      <polygon points="0,0 520,0 0,300" fill="url(#metal)"/>
      <polygon points="700,0 900,0 900,115 500,110" fill="var(--graphite)"/>
      <polygon points="0,250 330,100 900,130 900,300 0,270" fill="var(--band-silver)"/>
      <polygon points="330,100 0,250 0,270 200,160" fill="url(#fold-shade)"/>
      <polygon points="270,290 900,310 900,410 60,330" fill="var(--graphite)"/>
    </svg>
    <p class="wordmark">Brell Harbor Company</p>
    <div class="front-web">
      <svg viewBox="0 0 34 34"><g fill="none" stroke="var(--white)" stroke-width="2"><circle cx="17" cy="17" r="15"/><ellipse cx="17" cy="17" rx="7" ry="15"/><line x1="2" y1="17" x2="32" y2="17"/><line x1="4" y1="10" x2="30" y2="10"/><line x1="4" y1="24" x2="30" y2="24"/></g></svg>
      www.brellharbor-example.com
    </div>
  </section>

</div>
</body>
</html>
```